Lantern Method of Ascent Programme Graphic

Please refer to attached graphic.
I wish to redesign this graphic to represent a programme of work that we (Vendro) deliver to our customers.
The design represents 9 steps ( 3 steps at each of 3 levels) and is all about implementing the 'Lantern Method of Ascent'

I like the fact that the increasing business growth is evident when you are progressing through the stages, but the current graphic looks dated and the colours are not working.
I would also like to incorporate the LMA logo we have created.

Target Market(s)

IT Sector - businesses looking to grow

Industry/Entity Type

We are a digital marketing company

Requirements
Must have
• Clear, concise design
Should not have
• Design must not be complicated

```html
<!DOCTYPE html>
<html lang="en">
<head>
<meta charset="utf-8">
<title>Business Value – Lantern Method of Ascent</title>
<link rel="stylesheet" href="https://fonts.googleapis.com/css2?family=Ubuntu:wght@400;500&display=swap">
<style>
  :root {
    --page: #f4f7fb;
    --ink: #0d2340;
    --ink-soft: #5a6b82;
    --line: #9fb0c6;
    --white: #ffffff;
    --stage1: #6ccfc3;
    --stage1-deep: #48b5a8;
    --stage2: #1fa093;
    --stage2-deep: #15867b;
    --stage3: #0b6b66;
    --stage3-deep: #074f4c;
    --accent: #ff7a59;
    --band: #0d2340;
    --pill: rgba(255,255,255,0.2);
  }
  * { margin: 0; padding: 0; box-sizing: border-box; }
  html, body { width: 1200px; height: 755px; overflow: hidden; }
  body {
    position: relative;
    font-family: "Ubuntu", sans-serif;
    font-weight: 400;
    color: var(--white);
    background: var(--page);
  }
  .abs { position: absolute; }

  .title-pill {
    left: 35px; top: 19px; width: 342px; height: 60px;
    border-radius: 30px;
    border: 2px solid var(--ink);
    display: flex; align-items: center; justify-content: center;
    font-size: 34px; font-weight: 500; letter-spacing: 1px;
    color: var(--ink);
  }

  .growth-line { left: 0; top: 0; }

  .stage-block { border-radius: 22px 22px 0 0; overflow: hidden; }
  .stage-block .footer {
    position: absolute; left: 0; right: 0; bottom: 0; height: 82px;
    padding-left: 22px;
    display: flex; flex-direction: column; justify-content: center;
    font-size: 19px; line-height: 1.3; font-weight: 500;
  }
  .block-1 { left: 244px; top: 441px; width: 273px; height: 234px; background: var(--stage1); }
  .block-1 .footer { background: var(--stage1-deep); }
  .block-2 { left: 539px; top: 361px; width: 274px; height: 314px; background: var(--stage2); }
  .block-2 .footer { background: var(--stage2-deep); }
  .block-3 { left: 835px; top: 279px; width: 273px; height: 396px; background: var(--stage3); }
  .block-3 .footer { background: var(--stage3-deep); }

  .stage-heading {
    height: 52px; border-radius: 26px;
    display: flex; align-items: center; justify-content: center;
    font-size: 27px; font-weight: 500; letter-spacing: 0.5px;
  }
  .heading-1 { left: 290px; top: 369px; width: 181px; background: var(--stage1); }
  .heading-2 { left: 574px; top: 290px; width: 204px; background: var(--stage2); }
  .heading-3 { left: 869px; top: 210px; width: 205px; background: var(--stage3); }

  .step-badge {
    width: 76px; height: 76px; border-radius: 50%;
    display: flex; align-items: center; justify-content: center;
    font-size: 42px; font-weight: 500;
    background: var(--white);
    border: 4px solid currentColor;
  }
  .badge-1 { left: 342px; top: 274px; color: var(--stage1-deep); }
  .badge-2 { left: 638px; top: 194px; color: var(--stage2); }
  .badge-3 { left: 933px; top: 114px; color: var(--stage3); }

  .item-list { list-style: none; }
  .item { display: flex; align-items: center; height: 34px; margin-bottom: 14px; }
  .item .dot { width: 9px; height: 9px; border-radius: 50%; background: var(--accent); margin-right: 14px; flex: none; }
  .item .label {
    height: 34px; border-radius: 17px;
    padding: 0 16px; display: flex; align-items: center;
    font-size: 19px; font-weight: 500; letter-spacing: 0.3px;
    background: var(--pill);
  }

  .bottom-band { left: 0; top: 683px; width: 1200px; height: 72px; background: var(--band); }
  .brand { display: flex; align-items: center; font-size: 22px; font-weight: 500; color: var(--white); }
  .brand .mark { width: 18px; height: 18px; background: var(--accent); margin-right: 10px; }
  .brand-method { left: 936px; top: 706px; }
  .brand-company { left: 1050px; top: 706px; }
</style>
</head>
<body>
  <div class="abs title-pill">BUSINESS VALUE</div>

  <svg class="abs growth-line" width="1200" height="755" viewBox="0 0 1200 755" aria-hidden="true">
    <g fill="none" stroke="var(--line)" stroke-width="2">
      <polyline points="428,312 528,302 630,243"/>
      <polyline points="724,231 826,221 926,163"/>
      <polyline points="1018,140 1075,60"/>
      <polyline points="1063,64 1075,60 1077,73"/>
    </g>
    <g fill="var(--accent)">
      <circle cx="528" cy="302" r="5"/>
      <circle cx="826" cy="221" r="5"/>
    </g>
  </svg>

  <section class="stage stage-1">
    <div class="abs stage-block block-1">
      <div class="footer"><span>NUMBERS THAT MATTER</span><span>FOUNDATION METRICS</span></div>
    </div>
    <div class="abs stage-heading heading-1">RHYTHMIC</div>
    <div class="abs step-badge badge-1">1</div>
    <ul class="abs item-list" style="left:268px; top:458px;">
      <li class="item"><span class="dot"></span><span class="label">PERSONAS</span></li>
      <li class="item"><span class="dot"></span><span class="label">DATABASE</span></li>
      <li class="item"><span class="dot"></span><span class="label">SYSTEMS</span></li>
    </ul>
  </section>

  <section class="stage stage-2">
    <div class="abs stage-block block-2">
      <div class="footer"><span>WEEKLY SCOREDCARD</span><span>TACTICAL EXECUTION</span></div>
    </div>
    <div class="abs stage-heading heading-2">ACQUISITION</div>
    <div class="abs step-badge badge-2">2</div>
    <ul class="abs item-list" style="left:563px; top:380px;">
      <li class="item"><span class="dot"></span><span class="label">MESSAGING</span></li>
      <li class="item"><span class="dot"></span><span class="label">LEADS</span></li>
      <li class="item"><span class="dot"></span><span class="label">PIPELINE</span></li>
    </ul>
  </section>

  <section class="stage stage-3">
    <div class="abs stage-block block-3">
      <div class="footer"><span>MONTHLY SCORECARD</span><span>STRATEGIC REVIEW</span></div>
    </div>
    <div class="abs stage-heading heading-3">CUSTOMERS</div>
    <div class="abs step-badge badge-3">3</div>
    <ul class="abs item-list" style="left:859px; top:300px;">
      <li class="item"><span class="dot"></span><span class="label">SALES</span></li>
      <li class="item"><span class="dot"></span><span class="label">NURTURE</span></li>
      <li class="item"><span class="dot"></span><span class="label">REFERENCE</span></li>
    </ul>
  </section>

  <div class="abs bottom-band"></div>
  <div class="abs brand brand-method"><span class="mark"></span>LMA</div>
  <div class="abs brand brand-company">Vendro</div>
</body>
</html>
```